Quick Banner Ad Job for IT Services Company

Need a collection of banner ads based around a common theme and message.

Main Theme.

IT Support and Managed Services - IT support you can rely on.
Free remote monitoring and alerting*
*conditions apply <-- this in small text

Secondary Content

Our customers are attracted by our exceptional level of customer service and trust us in providing them with support and advice over a long term relationship.

Note:
* Logos and colours attached. Only use these colours.
* Font is to be Myriad Pro

* Delivery will require the following sizes.
Leaderboard: 728×90
Medium Rectangle: 300×250
Wide Skyscraper: 160×600

Do the initial draft in leaderboard, other sizes can be worked once we have an agreed design for the main

Final delivery will also need to be in an editable format, not just final images.

Industry/Entity Type

It Company

```html
<!DOCTYPE html>
<html lang="en">
<head>
<meta charset="utf-8">
<title>IT Support and Managed Services – Leaderboard</title>
<link href="https://fonts.googleapis.com/css2?family=Source+Sans+3:ital,wght@0,400;0,600;0,700;1,400;1,600&display=swap" rel="stylesheet">
<style>
  :root {
    --navy: #0c2340;
    --navy-deep: #071a33;
    --blue: #1f5d99;
    --sky: #4a90cf;
    --white: #ffffff;
  }
  * { margin: 0; padding: 0; box-sizing: border-box; }
  html, body { width: 1200px; height: 148px; overflow: hidden; background: var(--white); }
  .banner {
    position: relative;
    width: 1200px;
    height: 148px;
    overflow: hidden;
    background: var(--white);
    font-family: "Source Sans 3", "Myriad Pro", sans-serif;
  }
  .backdrop { position: absolute; inset: 0; }
  .headline {
    position: absolute;
    left: 34px;
    top: -4px;
    font-size: 35px;
    font-weight: 700;
    color: var(--navy);
    letter-spacing: 0.2px;
    white-space: nowrap;
  }
  .taglines {
    position: absolute;
    top: 40px;
    left: 0;
    font-size: 15px;
    font-weight: 600;
    color: var(--navy);
    white-space: nowrap;
  }
  .taglines span { position: absolute; top: 0; }
  .tag-reliable { left: 58px; }
  .tag-offer { left: 296px; }
  .tag-conditions { left: 626px; }
  .message {
    position: absolute;
    left: 16px;
    top: 84px;
    width: 900px;
    font-size: 20px;
    line-height: 27px;
    font-style: italic;
    color: var(--white);
  }
  .brand {
    position: absolute;
    left: 1000px;
    top: 60px;
    display: flex;
    align-items: center;
    gap: 10px;
  }
  .brand-dot {
    width: 26px; height: 26px;
    border-radius: 50%;
    background: var(--blue);
  }
  .brand-name {
    font-size: 36px;
    font-weight: 700;
    color: var(--navy);
    line-height: 1;
  }
  .brand-sub {
    position: absolute;
    left: 1108px;
    top: 104px;
    font-size: 15px;
    font-weight: 600;
    color: var(--navy);
  }
</style>
</head>
<body>
<div class="banner">
  <svg class="backdrop" width="1200" height="148" viewBox="0 0 1200 148" aria-hidden="true">
    <defs>
      <linearGradient id="bandFill" x1="0" y1="0" x2="1" y2="0">
        <stop offset="0" stop-color="#0a2547"/>
        <stop offset="0.55" stop-color="#123a66"/>
        <stop offset="1" stop-color="#1f5d99"/>
      </linearGradient>
    </defs>
    <path class="band" d="M0,70 C300,60 650,58 900,66 C940,68 960,90 950,148 L0,148 Z" fill="url(#bandFill)"/>
    <path class="band-highlight" d="M0,70 C300,60 650,58 900,66 C930,67 948,80 952,100 C940,82 920,76 890,74 C650,66 300,66 0,76 Z" fill="var(--sky)" opacity="0.55"/>
    <path class="brand-panel" d="M985,0 L1200,0 L1200,148 L962,148 C976,110 1000,45 985,0 Z" fill="var(--white)"/>
    <path class="brand-panel-edge" d="M985,0 C1000,45 976,110 962,148" fill="none" stroke="var(--blue)" stroke-width="3"/>
  </svg>

  <h1 class="headline">IT Support and Managed Services</h1>
  <p class="taglines">
    <span class="tag-reliable">IT support you can rely on.</span>
    <span class="tag-offer">Free remote monitoring and alerting*</span>
    <span class="tag-conditions">*conditions apply</span>
  </p>
  <p class="message">Our customers are attracted by our exceptional level of customer service and trust us in providing the with support and advice over a long term relationship.</p>

  <div class="brand">
    <span class="brand-dot"></span>
    <span class="brand-name">NorvaLink</span>
  </div>
  <span class="brand-sub">IT Support</span>
</div>
</body>
</html>
```